Webdesign für Holding-Firma
Zielgruppe
Die velunto Holding ist eine Holding-Firma mit drei Tochtergesellschaften: velunto trusted advisors, velutno Real estate und Velunto GmbH. Wir haben Beteiligungen in IT-Unternehmen, Real Estate sowie kleine und mittlere Startups.
Aufgabenstellung
Das Design sollte nicht zu bunt sein und eher schlicht und futuristisch gestaltet sein. Gerne können die Farben aus den verschiedenen Logos verarbeitet werden.

```html
<!DOCTYPE html>
<html lang="de">
<head>
<meta charset="utf-8">
<title>Velunto Trusted Advisors</title>
<link href="https://fonts.googleapis.com/css2?family=Roboto:wght@300;400;500&family=Roboto+Condensed:wght@700&family=Open+Sans:wght@400;600&display=swap" rel="stylesheet">
<style>
  :root {
    --gold: #dfa043;
    --gold-light: #f2c84b;
    --ink: #2b2b2b;
    --text: #3a3a3a;
    --muted: #6a6a6a;
    --topbar: #f0f0f0;
    --rule: #b9b9b9;
    --white: #ffffff;
  }
  * { margin: 0; padding: 0; box-sizing: border-box; }
  html, body { width: 1200px; height: 1200px; overflow: hidden; background: var(--white); }
  body { position: relative; font-family: "Roboto", Arial, sans-serif; color: var(--text); }

  .topbar { position: absolute; top: 0; left: 0; width: 1200px; height: 35px; background: var(--topbar); border-bottom: 1px solid #e2e2e2; font-size: 12px; color: var(--muted); }
  .topbar .site { position: absolute; left: 163px; top: 10px; }
  .topbar .mail { position: absolute; right: 161px; top: 8px; font-size: 14px; letter-spacing: .3px; }

  .header { position: absolute; top: 35px; left: 0; width: 1200px; height: 86px; background: var(--white); }
  .brand { position: absolute; left: 163px; top: 23px; display: flex; align-items: center; gap: 12px; }
  .brand-mark { width: 34px; height: 34px; background: var(--gold-light); }
  .brand-name { font-weight: 500; font-size: 30px; color: var(--ink); letter-spacing: .5px; line-height: 1; }
  .phone { position: absolute; left: 555px; top: 25px; display: flex; align-items: center; gap: 10px; font-size: 22px; font-weight: 300; color: var(--ink); }
  .lang { position: absolute; right: 160px; top: 32px; font-size: 14px; letter-spacing: 1.5px; color: var(--ink); }

  .hero { position: absolute; top: 121px; left: 0; width: 1200px; height: 395px; overflow: hidden;
    background: linear-gradient(100deg, #c99a55 0%, #dcb377 35%, #e6c99a 55%, #d9b36e 78%, #c9a645 100%); }
  .hero-title { position: absolute; left: 172px; top: 131px; color: var(--white); font-family: "Open Sans", Arial, sans-serif; }
  .hero-title .big { display: block; font-size: 66px; font-weight: 600; line-height: 1; letter-spacing: -1px; }
  .hero-title .sub { display: block; font-size: 33px; font-weight: 400; line-height: 1; margin-top: 0; margin-left: 4px; }

  .section-title { position: absolute; font-family: "Roboto Condensed", Arial, sans-serif; font-weight: 700; font-size: 27px; color: var(--gold); letter-spacing: .3px; }
  .body-text { position: absolute; font-size: 13.6px; font-weight: 300; line-height: 22.5px; color: var(--text); }

  .services { position: absolute; top: 746px; left: 163px; width: 880px; height: 70px; }
  .services ul { position: absolute; top: 0; list-style: none; }
  .services li { display: flex; align-items: center; height: 22.5px; font-size: 14px; font-weight: 300; color: var(--text); }
  .services svg { width: 20px; height: 16px; margin-right: 14px; }

  .footer { position: absolute; top: 996px; left: 0; width: 1200px; height: 204px;
    background: linear-gradient(120deg, #e9e9e9 0%, #dfdfdf 40%, #e8e8e8 70%, #dcdcdc 100%); overflow: hidden; }
  .footer-col { position: absolute; top: 22px; font-size: 14.5px; line-height: 19.5px; letter-spacing: .4px; color: var(--ink); }
  .footer-col strong { font-weight: 500; }
  .footer-rule { position: absolute; left: 161px; top: 152px; width: 879px; height: 1px; background: var(--rule); }
  .copyright { position: absolute; top: 168px; left: 0; width: 1200px; text-align: center; font-size: 12px; font-weight: 300; color: var(--ink); }
</style>
</head>
<body>
  <div class="topbar">
    <span class="site">www.norvik-systeme.de</span>
    <span class="mail">kontakt@velunto.de</span>
  </div>

  <header class="header">
    <div class="brand">
      <span class="brand-mark"></span>
      <span class="brand-name">VELUNTO</span>
    </div>
    <div class="phone">
      <svg width="24" height="18" viewBox="0 0 24 18" aria-hidden="true">
        <path d="M1 6 C1 1 23 1 23 6 L23 8 L17 8 L17 5 L7 5 L7 8 L1 8 Z" fill="#333"/>
        <path d="M5 9 L19 9 L22 17 L2 17 Z" fill="#333"/>
        <circle cx="12" cy="13" r="2.2" fill="#fff"/>
      </svg>
      <span>+49 (7000) 410 226 58</span>
    </div>
    <div class="lang">DE &nbsp;|&nbsp; EN</div>
  </header>

  <section class="hero" role="img" aria-label="Foto: Beratungsgespräch am Schreibtisch mit Taschenrechner, Notizblock und Unterlagen, warm goldgetönt">
    <div class="hero-title">
      <span class="big">VELUNTO</span>
      <span class="sub">TRUSTED ADVISORS</span>
    </div>
  </section>

  <h2 class="section-title" style="left:163px; top:553px;">WER SIND WIR?</h2>
  <p class="body-text" style="left:163px; top:597px; width:880px;">Wir sind ein Unternehmen VELUNTO group und sehen uns als strategische Berater und Planer, professioneller Manager, Controller, Backoffice-Dienstleister und Finanzberater und vieles mehr...</p>

  <h2 class="section-title" style="left:163px; top:703px;">WAS TUN WIR?</h2>
  <div class="services">
    <ul style="left:0;">
      <li><svg viewBox="0 0 20 16"><path d="M1 8 L7 14 L19 2" stroke="#333" stroke-width="4" fill="none"/></svg>Wealth management</li>
      <li><svg viewBox="0 0 20 16"><path d="M1 8 L7 14 L19 2" stroke="#333" stroke-width="4" fill="none"/></svg>Investitionen</li>
      <li><svg viewBox="0 0 20 16"><path d="M1 8 L7 14 L19 2" stroke="#333" stroke-width="4" fill="none"/></svg>Beteiligungsmanagement</li>
    </ul>
    <ul style="left:335px;">
      <li><svg viewBox="0 0 20 16"><path d="M1 8 L7 14 L19 2" stroke="#333" stroke-width="4" fill="none"/></svg>Immobilienmanagement</li>
      <li><svg viewBox="0 0 20 16"><path d="M1 8 L7 14 L19 2" stroke="#333" stroke-width="4" fill="none"/></svg>Familiy governance</li>
      <li><svg viewBox="0 0 20 16"><path d="M1 8 L7 14 L19 2" stroke="#333" stroke-width="4" fill="none"/></svg>Vermögensplanung</li>
    </ul>
    <ul style="left:704px;">
      <li><svg viewBox="0 0 20 16"><path d="M1 8 L7 14 L19 2" stroke="#333" stroke-width="4" fill="none"/></svg>Strukturen</li>
      <li><svg viewBox="0 0 20 16"><path d="M1 8 L7 14 L19 2" stroke="#333" stroke-width="4" fill="none"/></svg>Nachfolgeplanung</li>
      <li><svg viewBox="0 0 20 16"><path d="M1 8 L7 14 L19 2" stroke="#333" stroke-width="4" fill="none"/></svg>Finanzdienstleistungen</li>
    </ul>
  </div>

  <h2 class="section-title" style="left:161px; top:865px;">UNSER ANSPRUCH</h2>
  <p class="body-text" style="left:162px; top:907px; width:900px;">Wir sind für Sie da, damit Sie sich befreit, gesichert und mit voller Konzentration auf Ihre Funktion im eigenen Unternehmen fokussieren können.</p>

  <footer class="footer">
    <div class="footer-col" style="left:517px;">
      <strong>VELUNTO holding GmbH</strong><br>
      Lindenweg 14<br>
      77000 Musterstadt<br>
      kontakt@velunto.de<br>
      +49 (7000) 410 226 58
    </div>
    <div class="footer-col" style="left:789px;">
      <strong>Rechtliches:</strong><br>
      GF: Jonas Keller und Lena Keller<br>
      HRB 712384<br>
      Steuer-Nr.: 14000/52817
    </div>
    <div class="footer-rule"></div>
    <p class="copyright">Copyright 2020. All rights reserved.</p>
  </footer>
</body>
</html>
```